Kelvora IT company focused on 3 areas of IT

Looking for something similar to attached cards. Logo for kelvora also attached.. Looking for something clean as far as colors (surprise me).. kelvo stands for 3 primary areas, web design, consulting and network infrastructure design. Please email me if you have any questions. Looking forward to seeing how creative and professional this card will look. Thank you,

Target Market(s)

Small business/consumers looking for It services

Industry/Entity Type

It Service

Contact Information for Business Card

Dorian Vesk
Principal Consultant

202-555-0173

www.kelvora-example.com
dvesk@kelvora-example.com

4172 Marsh Lantern Ct,
Larkmoor, ST 00000

Colors

Designer to choose colors to be used in the design.

Requirements
Must have
• attached Logo design. Feel free to play with the colors.. If you have a better idea for a card, please fee free to send me. Looking for something clean/modern. Should have tech feel, not cheesy.
Nice to have
• Surprise me :-)..

```html
<!DOCTYPE html>
<html lang="en">
<head>
<meta charset="utf-8">
<title>Kelvora Business Card</title>
<link href="https://fonts.googleapis.com/css2?family=Lato:wght@300;400;700;900&display=swap" rel="stylesheet">
<style>
  :root {
    --ink: #231f20;
    --card-dark: #2b2a2a;
    --paper: #ffffff;
    --stage: #d8d8d8;
    --logo-ink: #1f2a2e;
  }
  * { box-sizing: border-box; margin: 0; padding: 0; }
  html, body {
    width: 1200px; height: 900px; overflow: hidden;
    background: var(--stage);
    font-family: 'Lato', sans-serif;
  }
  .canvas { position: relative; width: 1200px; height: 900px; }

  .card { position: absolute; border-radius: 14px; overflow: hidden; }

  /* Front */
  .card-front {
    left: 70px; top: 290px; width: 560px; height: 320px;
    background: var(--card-dark); color: var(--paper);
    display: flex; flex-direction: column; align-items: center; justify-content: center;
  }
  .brand { display: flex; align-items: center; gap: 12px; }
  .brand-square { width: 18px; height: 18px; background: currentColor; }
  .brand-name { font-weight: 900; font-size: 40px; letter-spacing: 3px; text-transform: uppercase; }
  .front-web {
    margin-top: 56px; font-weight: 700; font-size: 13px; letter-spacing: 3px;
  }

  /* Back */
  .card-back {
    left: 760px; top: 170px; width: 330px; height: 560px;
    background: var(--paper); color: var(--ink);
    display: flex; flex-direction: column;
  }
  .back-logo {
    height: 190px; display: flex; align-items: center; justify-content: center;
    color: var(--logo-ink);
  }
  .back-logo .brand-name { font-size: 34px; }
  .name-band {
    height: 110px; background: var(--card-dark); color: var(--paper);
    display: flex; flex-direction: column; justify-content: center; padding-left: 34px;
  }
  .person-name { font-size: 30px; text-transform: uppercase; letter-spacing: 0.5px; }
  .person-name .first { font-weight: 900; }
  .person-name .last { font-weight: 300; }
  .person-title { font-size: 20px; font-weight: 300; margin-top: 4px; }
  .contact-list { list-style: none; padding: 34px 0 0 34px; }
  .contact-item { display: flex; align-items: flex-start; gap: 14px; margin-bottom: 22px; font-size: 17px; line-height: 1.25; }
  .contact-icon {
    flex: none; width: 26px; height: 26px; background: var(--ink);
    display: flex; align-items: center; justify-content: center;
  }
  .contact-icon svg { width: 16px; height: 16px; }
</style>
</head>
<body>
<main class="canvas">
  <section class="card card-front">
    <div class="brand">
      <span class="brand-square"></span>
      <span class="brand-name">Kelvora</span>
    </div>
    <p class="front-web">www.kelvora-example.com</p>
  </section>

  <section class="card card-back">
    <div class="back-logo">
      <div class="brand">
        <span class="brand-square"></span>
        <span class="brand-name">Kelvora</span>
      </div>
    </div>
    <div class="name-band">
      <p class="person-name"><span class="first">Dorian</span> <span class="last">Vesk</span></p>
      <p class="person-title">Principal Consultant</p>
    </div>
    <ul class="contact-list">
      <li class="contact-item">
        <span class="contact-icon"><svg viewBox="0 0 16 16"><path fill="#fff" d="M3 1.5h3l1 3.5-2 1.2a8 8 0 0 0 4.8 4.8L11 9l3.5 1v3c0 .8-.7 1.5-1.5 1.5C7 14.5 1.5 9 1.5 3 1.5 2.2 2.2 1.5 3 1.5z"/></svg></span>
        <span>202-555-0173</span>
      </li>
      <li class="contact-item">
        <span class="contact-icon"><svg viewBox="0 0 16 16"><rect x="1.5" y="3.5" width="13" height="9" fill="none" stroke="#fff" stroke-width="1.4"/><path d="M1.5 3.5 8 9l6.5-5.5" fill="none" stroke="#fff" stroke-width="1.4"/></svg></span>
        <span>dvesk@kelvora-example.com</span>
      </li>
      <li class="contact-item">
        <span class="contact-icon"><svg viewBox="0 0 16 16"><path fill="#fff" d="M8 1a5 5 0 0 0-5 5c0 3.6 5 9 5 9s5-5.4 5-9a5 5 0 0 0-5-5zm0 7a2 2 0 1 1 0-4 2 2 0 0 1 0 4z"/></svg></span>
        <span>4172 Marsh Lantern Ct,<br>Larkmoor, ST 00000</span>
      </li>
    </ul>
  </section>
</main>
</body>
</html>
```